Full book cover design for DIALOGUE book

The book title is: Dialogue
Subtitle: Ask it, share it, grow with it.
Authors: Carl Brenner & Marian Quist
We are looking for a complete book cover design using a combination of my brand colours and that of my co-author (Carl). The colours we use include:

Marian: Blue #1E84AB & Carl: Blue #01275B and white.

An idea on the wording for the back cover is here (open to tweak/shorten it if better that way):

The most dynamic leaders today are focused on increasing effectiveness and improving team cohesion. This book demonstrates how creating a culture of feedback enables both of these things.

Dialogue allows for the strengthening of communication and allows individuals to continually learn and grow, with the support of their colleagues.

Marian and Carl have created a unique approach to change the often-negative perception associated with feedback. They created it for you…to unlock the opportunity, freedom and success you can achieve when feedback is implemented and used regularly.

If you are a leader looking for ways to build skills in your people, contribute to their growth and development, and maintain a strong, supportive culture, all while delivering business outcomes, then this is the book for you.

“If you are keen to transform feedback from average to awesome and from being a chore to an art, this book is a must read.”
Victor Lunsky, Bravelane Axton

“In today’s hybrid work environment, greater transparency and empowerment, through developing a feedback culture, is essential.”
Odette Varley, Pelvro

We will also need to allow space for a barcode and the publishers logo (just above it) on the back bottom right hand side.

Target Market(s)

Business leaders

Industry/Entity Type

Business

Font styles to use
Serif
Other font styles liked:
• Open to any other fonts that will suit the design

Colors
0054AA
0677BA
7BADD7
CADEEF
E8F1F8

Requirements
Must have
• Colours: Blue #1E84AB & Blue #01275B and white.
Nice to have
• Something creative and smart but not too busy.

```html
<!DOCTYPE html>
<html lang="en">
<head>
<meta charset="utf-8">
<title>Dialogue – Book Cover</title>
<link rel="stylesheet" href="https://fonts.googleapis.com/css2?family=Hind:wght@400;500;600&display=swap">
<style>
  :root {
    --navy: #01275B;
    --teal: #1E84AB;
    --mid-blue: #0677BA;
    --pale-blue: #CADEEF;
    --paper: #FFFFFF;
    --backdrop: #EFEFEF;
    --strip-shadow: rgba(0, 0, 0, 0.18);
  }
  * { margin: 0; padding: 0; box-sizing: border-box; }
  html, body {
    width: 1200px;
    height: 800px;
    overflow: hidden;
    background: var(--backdrop);
    font-family: "Hind", sans-serif;
  }
  .stage {
    position: relative;
    width: 1200px;
    height: 800px;
  }
  .cover {
    position: absolute;
    left: 360px;
    top: 30px;
    width: 480px;
    height: 740px;
    background: linear-gradient(180deg, #FFFFFF 0%, #F6F6F6 100%);
    box-shadow: 0 10px 30px rgba(0, 0, 0, 0.12);
    overflow: hidden;
  }
  .chat-cluster {
    position: absolute;
    left: 98px;
    top: 120px;
    width: 245px;
    height: 240px;
  }
  .chat-cluster svg { width: 100%; height: 100%; display: block; }
  .title {
    position: absolute;
    left: 0;
    right: 0;
    top: 368px;
    text-align: center;
    font-weight: 600;
    font-size: 88px;
    line-height: 1;
    letter-spacing: -3px;
    background: linear-gradient(90deg, var(--navy) 0%, var(--teal) 70%, var(--navy) 100%);
    -webkit-background-clip: text;
    background-clip: text;
    color: transparent;
  }
  .subtitle-strip {
    position: absolute;
    left: 62px;
    top: 516px;
    width: 358px;
    height: 60px;
    background: var(--paper);
    box-shadow: 0 4px 10px var(--strip-shadow);
    display: flex;
    align-items: center;
    justify-content: center;
  }
  .subtitle {
    font-weight: 500;
    font-size: 18px;
    letter-spacing: 0.4px;
    color: var(--navy);
    text-transform: uppercase;
    padding-top: 3px;
    white-space: nowrap;
  }
  .author-band {
    position: absolute;
    left: 0;
    right: 0;
    top: 642px;
    height: 58px;
    background: var(--navy);
    display: flex;
    align-items: center;
    justify-content: center;
  }
  .authors {
    color: var(--paper);
    font-weight: 400;
    font-size: 26px;
    padding-top: 4px;
    white-space: nowrap;
  }
</style>
</head>
<body>
  <main class="stage">
    <section class="cover">
      <div class="chat-cluster">
        <svg viewBox="0 0 258 242" role="img" aria-label="Speech bubble made of many small chat and message icons in navy and teal">
          <defs>
            <linearGradient id="clusterTone" x1="0" y1="0" x2="1" y2="1">
              <stop offset="0" stop-color="#01275B"/>
              <stop offset="0.55" stop-color="#1E84AB"/>
              <stop offset="1" stop-color="#7BADD7"/>
            </linearGradient>
          </defs>
          <path d="M18 10 H240 Q252 10 252 22 V178 Q252 190 240 190 H222 L250 238 L196 190 H18 Q6 190 6 178 V22 Q6 10 18 10 Z" fill="url(#clusterTone)"/>
        </svg>
      </div>

      <h1 class="title">Dialogue</h1>

      <div class="subtitle-strip">
        <p class="subtitle">Ask it, share it, grow with it</p>
      </div>

      <div class="author-band">
        <p class="authors">Carl Brenner &amp; Marian Quist</p>
      </div>
    </section>
  </main>
</body>
</html>
```